Statonary for Design Build Firm
Design Build company
Statonary for Design Build Firm -
Creative Brief
Professional
Peter L. Vondrasek
C.E.O.
Sharjah UAE
US# 1-415-372-9054
mvelondrask@tmwrgroup.net
www.tmwrgroup.net

```html
<!DOCTYPE html>
<html lang="en">
<head>
<meta charset="utf-8">
<title>TMWR Group, Inc. – Business Card</title>
<link rel="stylesheet" href="https://fonts.googleapis.com/css2?family=Source+Sans+3:wght@600;700&display=swap">
<style>
  :root {
    --page: #ffffff;
    --card-edge: #1a1a1a;
    --navy-deep: #0a2a5c;
    --navy: #123f82;
    --cyan-glow: #46c6f0;
    --orange: #f58220;
    --brand-grey: #5f6670;
    --brand-blue: #1c5aa6;
    --text-light: #ffffff;
  }
  html, body {
    margin: 0;
    width: 1200px;
    height: 751px;
    overflow: hidden;
    background: var(--page);
  }
  .canvas {
    position: relative;
    width: 1200px;
    height: 751px;
  }
  .card {
    position: absolute;
    left: 72px;
    top: 77px;
    width: 1058px;
    height: 600px;
    border: 2px solid var(--card-edge);
    box-sizing: border-box;
    background: #fff;
    overflow: hidden;
    font-family: "Source Sans 3", "Myriad Pro", Arial, sans-serif;
  }
  .card__art {
    position: absolute;
    inset: 0;
    width: 100%;
    height: 100%;
  }
  .brand {
    position: absolute;
    left: 60px;
    top: 82px;
    display: flex;
    align-items: center;
    gap: 26px;
  }
  .brand__square {
    width: 96px;
    height: 96px;
    background: var(--brand-blue);
  }
  .brand__name {
    font-size: 52px;
    font-weight: 700;
    color: var(--brand-grey);
    letter-spacing: 1px;
    line-height: 1;
  }
  .contact {
    position: absolute;
    right: 55px;
    top: 292px;
    text-align: right;
    color: var(--text-light);
    font-weight: 700;
  }
  .contact__name {
    margin: 0;
    font-size: 40px;
    line-height: 46px;
  }
  .contact__title {
    margin: 0 0 22px;
    font-size: 34px;
    line-height: 40px;
  }
  .contact__lines {
    margin: 0;
    padding: 0;
    list-style: none;
    font-size: 24px;
    line-height: 29px;
  }
</style>
</head>
<body>
<div class="canvas">
  <div class="card">
    <svg class="card__art" viewBox="0 0 1058 600" preserveAspectRatio="none" aria-hidden="true">
      <defs>
        <radialGradient id="blueGlow" cx="500" cy="470" r="600" gradientUnits="userSpaceOnUse">
          <stop offset="0" stop-color="var(--cyan-glow)"/>
          <stop offset="0.45" stop-color="var(--navy)"/>
          <stop offset="1" stop-color="var(--navy-deep)"/>
        </radialGradient>
      </defs>
      <polygon class="band-orange" points="0,600 1058,62 1058,139 30,600" fill="var(--orange)"/>
      <polygon class="panel-blue" points="30,600 1058,139 1058,600" fill="url(#blueGlow)"/>
    </svg>

    <div class="brand">
      <div class="brand__square"></div>
      <div class="brand__name">TMWR GROUP, INC.</div>
    </div>

    <div class="contact">
      <p class="contact__name">Peter L. Vondrasek</p>
      <p class="contact__title">C.E.O.</p>
      <ul class="contact__lines">
        <li>Sharjah UAE</li>
        <li>Phone: US# 1-415-372-9054</li>
        <li>Cell: +971-(0)50-286-4173</li>
        <li>Email: mvelondrask@tmwrgroup.net</li>
        <li>www.tmwrgroup.net</li>
      </ul>
    </div>
  </div>
</div>
</body>
</html>
```